Calendar Ad / Flyer

Our law firm needs a calendar ad to place in a local calendar.
THE DEADLINE IS THIS THURSDAY 06/28/2018.

Attached is the ad used in last years calendar. A few notes on this...
**. This is by no means the model to follow.
Please be creative and do what makes more sense marketing wise.
1. Need to update the color scheme which corresponds to the new website at marvolinlegal.com
2. The "MARVOLIN LAW | SHAPING FAITH WITH RESULTS" should be put at the top and made larger
3. "KNOWN AND TRUSTED IN OUR COMMUNITY FOR OVER 21 YEARS" should be changed to "KNOWN AND TRUSTED IN OUR COMMUNITY FOR OVER 22 YEARS"
4. "Gordon R. Marvolin, Esq." should be made larger and better positioned.
5. Under the list of practices, it should be changed to have:
"Personal Injury, Legal Malpractice, Unlicensed Contractors, Medical Malpractice, Civil Litigation"
6. Contact information (i.e. contact number, website, and address) should be better positioned
7. Placement of endorsement logos should stand out more.
8. New picture of head attorney is attached.

Last but not least... Give it your best shot!

```html
<!DOCTYPE html>
<html lang="en">
<head>
<meta charset="utf-8">
<title>Marvolin Law Calendar Ad</title>
<link href="https://fonts.googleapis.com/css2?family=Roboto:wght@400;500;700&family=Cabin:wght@500&display=swap" rel="stylesheet">
<style>
  :root {
    --gold: #d3b185;
    --gold-dark: #b89566;
    --slate: #474c55;
    --slate-line: #3c4048;
    --wall: #f0f0f0;
    --wall-shade: #e2e2e2;
    --white: #ffffff;
  }
  html, body { margin: 0; padding: 0; overflow: hidden; background: #ffffff; }
  .ad {
    position: relative; width: 1200px; height: 900px; overflow: hidden;
    background: linear-gradient(180deg, var(--wall) 0%, var(--wall-shade) 100%);
    font-family: "Roboto", sans-serif; color: var(--slate);
  }
  .logo { position: absolute; left: 40px; top: 118px; }
  .logo-mark { position: absolute; left: 176px; top: -70px; width: 64px; height: 64px; background: var(--gold); }
  .logo-name { font-family: "Roboto", sans-serif; font-weight: 500; font-size: 38px; letter-spacing: 3px; color: var(--gold-dark); white-space: nowrap; }
  .logo-tagline { margin-top: 4px; padding-left: 86px; font-size: 12px; font-weight: 500; letter-spacing: 0.5px; color: var(--slate); white-space: nowrap; }
  .title-block { position: absolute; right: 68px; top: 44px; text-align: right; }
  .firm-title { margin: 0; font-size: 88px; font-weight: 500; line-height: 1; letter-spacing: 1px; color: var(--slate); white-space: nowrap; }
  .firm-tagline { margin: 8px 0 0; font-size: 35px; line-height: 1; color: #2b2e33; white-space: nowrap; }
  .firm-tagline strong { font-weight: 700; }
  .firm-tagline span { font-weight: 400; }
  .practice-band {
    position: absolute; left: 0; top: 248px; width: 1200px; height: 331px;
    background: var(--gold); border-top: 2px solid var(--slate-line); border-bottom: 2px solid var(--slate-line); box-sizing: border-box;
  }
  .headline { position: absolute; left: 38px; top: 36px; margin: 0; font-size: 46px; font-weight: 500; line-height: 50px; color: var(--white); }
  .headline em { font-style: normal; font-weight: 700; color: var(--slate); }
  .practice-list { position: absolute; margin: 0; padding: 0; list-style: none; font-family: "Cabin", sans-serif; font-weight: 500; font-size: 26px; color: var(--white); }
  .practice-list li { display: flex; align-items: center; height: 50px; }
  .practice-list svg { width: 24px; height: 24px; margin-right: 16px; }
  .list-left { left: 46px; top: 156px; }
  .list-right { left: 403px; top: 156px; }
  .name-pill {
    position: absolute; left: 434px; top: 622px; width: 500px; height: 78px;
    background: var(--slate); border-radius: 39px 0 0 39px;
    color: var(--white); font-size: 31px; font-weight: 500; line-height: 78px; padding-left: 44px; box-sizing: border-box; white-space: nowrap;
  }
  .attorney-photo {
    position: absolute; left: 850px; top: 186px; width: 350px; height: 564px;
    background: linear-gradient(180deg, #8d8f92 0%, #6a6d71 45%, #55585c 100%);
  }
  .footer { position: absolute; left: 0; top: 750px; width: 1200px; height: 150px; background: var(--slate); color: var(--white); }
  .contact-line { position: absolute; display: flex; align-items: center; white-space: nowrap; }
  .contact-line svg { margin-right: 12px; }
  .phone { left: 28px; top: 28px; font-size: 43px; font-weight: 700; }
  .web { left: 30px; top: 88px; font-size: 29px; font-weight: 500; }
  .address { left: 388px; top: 34px; align-items: flex-start; font-size: 22px; line-height: 27px; }
  .address svg { margin-top: 4px; margin-right: 10px; }
  .endorsements { position: absolute; left: 732px; top: 52px; display: flex; gap: 34px; align-items: center; }
  .badge { width: 58px; height: 58px; }
  .badge-round { border-radius: 50%; background: #9a2a2a; border: 3px solid #c7a24d; box-sizing: border-box; }
  .badge-stars { width: 84px; height: 50px; background: #8e8e8e; border-radius: 4px; }
  .badge-gold { width: 64px; height: 52px; background: #b9944f; border-radius: 4px; }
  .badge-blue { width: 62px; height: 54px; background: #1e5d8f; border-radius: 3px; }
  .badge-ring { border-radius: 50%; background: #ffffff; border: 6px solid #3d9bd6; box-sizing: border-box; }
</style>
</head>
<body>
<div class="ad">
  <div class="logo">
    <div class="logo-mark"></div>
    <div class="logo-name">MARVOLIN LAW</div>
    <div class="logo-tagline">SHAPING FAITH WITH RESULTS</div>
  </div>

  <div class="title-block">
    <h1 class="firm-title">MARVOLIN LAW</h1>
    <p class="firm-tagline"><strong>SHAPING FAITH</strong> <span>WITH RESULTS</span></p>
  </div>

  <section class="practice-band">
    <h2 class="headline">KNOWN AND TRUSTED IN OUR<br>COMMUNITY FOR OVER <em>22 YEARS</em></h2>
    <ul class="practice-list list-left">
      <li><svg viewBox="0 0 24 24" fill="none" stroke="#fff" stroke-width="2.4"><path d="M18 13v7H3V5h11"/><path d="M7 11l4 4 10-11"/></svg>Personal Injury</li>
      <li><svg viewBox="0 0 24 24" fill="none" stroke="#fff" stroke-width="2.4"><path d="M18 13v7H3V5h11"/><path d="M7 11l4 4 10-11"/></svg>Medical Malpractice</li>
      <li><svg viewBox="0 0 24 24" fill="none" stroke="#fff" stroke-width="2.4"><path d="M18 13v7H3V5h11"/><path d="M7 11l4 4 10-11"/></svg>Unlicensed Contractors</li>
    </ul>
    <ul class="practice-list list-right">
      <li><svg viewBox="0 0 24 24" fill="none" stroke="#fff" stroke-width="2.4"><path d="M18 13v7H3V5h11"/><path d="M7 11l4 4 10-11"/></svg>Legal Malpractice</li>
      <li><svg viewBox="0 0 24 24" fill="none" stroke="#fff" stroke-width="2.4"><path d="M18 13v7H3V5h11"/><path d="M7 11l4 4 10-11"/></svg>Civil Litigation</li>
    </ul>
  </section>

  <div class="name-pill">Gordon R. Marvolin, Esq.</div>

  <div class="attorney-photo" role="img" aria-label="Portrait photo of the head attorney in a grey suit and blue tie"></div>

  <footer class="footer">
    <div class="contact-line phone">
      <svg width="30" height="30" viewBox="0 0 24 24" fill="none" stroke="#fff" stroke-width="1.8"><circle cx="12" cy="12" r="10.5"/><path d="M8.5 6.5l2 2.5-1.2 1.5c.8 1.6 2 2.8 3.6 3.6l1.5-1.2 2.5 2-1.2 1.8c-3.8-.4-7.4-4-7.8-7.8z" fill="#fff"/></svg>
      310.555.0142
    </div>
    <div class="contact-line web">
      <svg width="24" height="24" viewBox="0 0 24 24" fill="none" stroke="#fff" stroke-width="1.6"><circle cx="12" cy="12" r="10"/><ellipse cx="12" cy="12" rx="4.5" ry="10"/><path d="M2 12h20M4 7h16M4 17h16"/></svg>
      www.marvolinlegal.com
    </div>
    <div class="contact-line address">
      <svg width="16" height="22" viewBox="0 0 16 22"><path d="M8 0a8 8 0 0 0-8 8c0 6 8 14 8 14s8-8 8-14a8 8 0 0 0-8-8zm0 11a3 3 0 1 1 0-6 3 3 0 0 1 0 6z" fill="#fff"/></svg>
      <span>8120 Corliss Blvd.,<br>Suite #302 Fairhaven,<br>CA 90317</span>
    </div>
    <div class="endorsements">
      <div class="badge badge-round"></div>
      <div class="badge badge-stars"></div>
      <div class="badge badge-gold"></div>
      <div class="badge badge-blue"></div>
      <div class="badge badge-ring"></div>
    </div>
  </footer>
</div>
</body>
</html>
```